Velmora Water Purification

We need a website set up on a "Free account" WordPress platform. (This is the type of Wordpress site that you can sign up for and create online for free (not a server-hosted type.)
The website will be for a water purification company. They install devices in homes to purify the water for safer drinking, bathing, and cleaning.
Our logo is attached. Please keep color scheme of the website consistent with the logo.
Water Purification

```html
<!DOCTYPE html>
<html lang="en">
<head>
<meta charset="utf-8">
<title>Velmora Water Purification</title>
<link rel="stylesheet" href="https://fonts.googleapis.com/css2?family=Roboto:wght@300;400;500&family=Poppins:wght@400;500;600&family=Open+Sans:ital,wght@1,400&display=swap">
<style>
:root{
  --navy:#1f2a78;
  --navy-dark:#17205e;
  --sky:#1a8dc4;
  --sky-light:#7dcdea;
  --ice:#e9f3fb;
  --ink:#333;
  --muted:#555;
  --footer:#1f1f1f;
  --footer-bar:#161616;
  --white:#fff;
}
*{box-sizing:border-box;margin:0;padding:0}
html,body{width:1200px;height:2426px;overflow:hidden}
body{position:relative;background:var(--white);font-family:"Poppins",sans-serif;color:var(--ink)}
.abs{position:absolute}

/* header */
.site-header{left:0;top:0;width:1200px;height:102px;background:linear-gradient(#fff,#dceefa);border-top:3px solid var(--sky)}
.brand{left:110px;top:30px;display:flex;align-items:center;gap:10px;font:500 30px "Roboto",sans-serif;color:var(--navy)}
.brand .dot{width:22px;height:22px;border-radius:50%;background:var(--sky)}
.call{right:112px;top:6px;text-align:left}
.call small{display:block;font:600 13px "Poppins",sans-serif;color:var(--sky);letter-spacing:.5px}
.call strong{font:400 22px "Roboto",sans-serif;color:var(--navy);letter-spacing:.3px}
.main-nav{left:343px;top:50px;width:745px;height:42px;border-radius:21px;background:linear-gradient(#2a3f9e,var(--navy-dark));display:flex;align-items:center;justify-content:space-around;padding:0 14px}
.main-nav a{font:500 13px "Poppins",sans-serif;color:var(--white);text-decoration:none;padding:6px 14px;border-radius:50%}
.main-nav a.active{border:2px solid #4d6fd6;border-radius:50%/60%}

/* hero */
.hero{left:0;top:102px;width:1200px;height:488px;background:linear-gradient(110deg,#4a4e52 0%,#8a9096 35%,#5d6369 60%,#9aa1a6 100%)}
.hero-title{left:0;width:1200px;top:248px;text-align:center;font:300 44px "Roboto",sans-serif;color:var(--white);letter-spacing:2px}
.hero-text{left:286px;top:386px;width:630px;text-align:center;font:500 12px/20px "Poppins",sans-serif;color:var(--white)}
.btn-estimate{left:496px;top:454px;width:206px;height:43px;border-radius:22px;background:linear-gradient(#2ea5dd,#167fb8);color:var(--white);font:500 13px "Poppins",sans-serif;display:flex;align-items:center;justify-content:center;letter-spacing:.3px}

/* welcome */
.welcome{left:0;top:590px;width:1200px;height:542px;background:linear-gradient(#fff 62%,#e4f1fa 80%,#c6e2f4 100%)}
.section-title{font:400 26px "Roboto",sans-serif;color:var(--sky)}
.section-title span{color:var(--navy)}
.welcome .section-title{left:110px;top:44px}
.welcome .rule{left:110px;top:88px;width:585px;height:1px;background:#d8d8d8}
.welcome p{left:110px;width:590px;font:400 11.5px/19.6px "Poppins",sans-serif;color:var(--ink)}
.btn-more{height:25px;border-radius:13px;background:#141414;color:var(--white);font:500 11px "Poppins",sans-serif;display:flex;align-items:center;padding-left:14px}
.btn-more::after{content:"";position:absolute;right:-4px;top:1px;width:18px;height:22px;border-radius:50% 50% 50% 50%/60% 60% 40% 40%;background:linear-gradient(#6ab9e8,var(--navy))}
.welcome .btn-more{left:110px;top:448px;width:86px}

.appointment{left:754px;top:52px;width:334px;height:438px;background:var(--ice);border:1px solid #bcd6ec}
.appointment h2{height:57px;background:var(--navy);color:var(--white);font:400 23px "Roboto",sans-serif;padding:14px 0 0 22px}
.appointment h2 span{color:#5fbbe9}
.field-label{left:17px;font:400 12px "Poppins",sans-serif;color:var(--ink)}
.field{left:17px;width:301px;height:36px;background:var(--white);border:1px solid #c9dceb;border-radius:3px}
.appointment .btn-more{left:17px;top:395px;width:88px}

/* services */
.services{left:0;top:1132px;width:1200px;height:412px;background:var(--sky-light)}
.center-title{left:0;width:1200px;text-align:center}
.divider{left:420px;width:360px;height:1px;background:rgba(255,255,255,.6)}
.drop{width:12px;height:16px;border-radius:50% 50% 50% 50%/60% 60% 40% 40%;background:linear-gradient(#7cc7ee,var(--navy))}
.service{width:300px;text-align:center}
.service-icon{width:170px;height:77px;margin:0 auto;display:block}
.service h3{margin-top:20px;font:400 17px "Roboto",sans-serif;color:var(--navy-dark)}
.service p{margin-top:6px;font:400 11.5px/19.6px "Poppins",sans-serif;color:var(--ink)}
.service .btn-more{position:relative;margin:22px auto 0;width:84px}

/* testimonials */
.testimonials .section-title{top:1590px}
.card{top:1742px;width:302px;height:216px;border:2px solid #e3e3e3;background:var(--white)}
.avatar{top:1685px;width:94px;height:107px}
.card blockquote{position:absolute;left:30px;right:30px;top:72px;text-align:center;font:italic 400 11.5px/22px "Open Sans",sans-serif;color:#666}
.card .q{font:700 22px "Roboto",sans-serif;color:#777;line-height:0;vertical-align:-6px}
.card hr{position:absolute;left:36px;right:36px;top:175px;border:0;border-top:1px solid #ddd}
.card cite{position:absolute;left:0;right:0;top:188px;text-align:center;font:500 12px "Poppins",sans-serif;font-style:normal;color:var(--navy)}

/* wave */
.wave{left:0;top:1930px;width:1200px;height:190px}
.wave-brand{left:0;width:1200px;top:2062px;text-align:center;font:500 26px "Roboto",sans-serif;color:var(--navy)}

/* footer */
.site-footer{left:0;top:2110px;width:1200px;height:251px;background:var(--footer)}
.footer-bar{left:0;top:2361px;width:1200px;height:65px;background:var(--footer-bar);border-top:1px solid #333}
.footer-heading{font:400 17px "Roboto",sans-serif;color:var(--white)}
.footer-rule{height:1px;background:#3a3a3a}
.quick-links{left:110px;top:2211px;list-style:none}
.quick-links li{font:400 11.5px/22px "Poppins",sans-serif;color:#ddd}
.quick-links li::before{content:"›";color:#888;margin-right:10px}
.contact-item{left:346px;display:flex;gap:12px;font:400 11.5px/16px "Poppins",sans-serif;color:#ddd}
.contact-item svg{flex:none;margin-top:1px}
.map{left:595px;top:2211px;width:222px;height:118px;background:linear-gradient(135deg,#d9e4c8,#f0e8c8 50%,#a9cbe4);border:2px solid #ccc}
.newsletter-text{left:875px;top:2210px;width:215px;font:400 11.5px/17px "Poppins",sans-serif;color:#ddd}
.newsletter-input{left:875px;top:2246px;width:181px;height:29px;background:var(--white);font:400 11px "Poppins",sans-serif;color:#777;padding:8px 8px}
.btn-subscribe{left:875px;top:2285px;width:95px;height:29px;background:#3d8fca;color:var(--white);font:500 12px "Poppins",sans-serif;display:flex;align-items:center;justify-content:center}
.social{width:26px;height:26px;border-radius:50%;background:var(--white);top:2380px}
.copyright{right:112px;top:2386px;font:400 11.5px "Poppins",sans-serif;color:#ddd}
</style>
</head>
<body>

<header class="site-header abs">
  <div class="brand abs"><span class="dot"></span>Velmora</div>
  <div class="call abs"><small>CALL US</small><strong>0100 555 0199</strong></div>
  <nav class="main-nav abs">
    <a class="active">About</a><a>Products</a><a>Free Estimates</a><a>Schedule An Appointment</a><a>Testimonials</a><a>Contact</a>
  </nav>
</header>

<section class="hero abs" role="img" aria-label="Photo of a glass being filled with water from a chrome kitchen tap"></section>
<h1 class="hero-title abs">VELMORA WATER PURIFICATION</h1>
<p class="hero-text abs">Lorem ipsum dolor sit amet, consectetuer adipiscing elit, sed diam nonummy nibh euismod tincidunt ut laoreet dolore magna aliquam erat volutpat. Ut wisi enim ad minim veniam.</p>
<div class="btn-estimate abs">REQUEST A FREE ESTIMATE</div>

<section class="welcome abs">
  <h2 class="section-title abs">Welcome to <span>Velmora</span></h2>
  <div class="rule abs"></div>
  <p class="abs" style="top:108px">Lorem ipsum dolor sit amet, consectetuer adipiscing elit, sed diam nonummy nibh euismod tincidunt ut laoreet dolore magna aliquam erat volutpat. Ut wisi enim ad minim veniam. dolor sit amet, consecuer adipiscing elit, sed diam nonummy nibh euismod tincidunt ut laoreet dolore magna aliquam erat vtpat. Ut wisi enim ad minim veniamdolor sit amet, consectetuer adipiscing elit, sed diam nonummy nibh euismod tincidunt ut laoreet dolore magna aliquam erat volutpat. Ut wisi enim ad minim. ut laoreet dolore magna aliquam erat volutpat. Ut wisi enim ad minim veniamdolor sit amet, consectetuer.</p>
  <p class="abs" style="top:245px">Lorem ipsum dolor sit amet, consectetuer adipiscing elit, sed diam nonummy nibh euismod tincidunt ut laoreet dolore magna aliquam erat volutpat. Ut wisi enim ad minim veniam. dolor sit amet, consecuer adipiscing elit, sed diam nonummy nibh euismod tincidunt ut laoreet dolore magna aliquam erat vtpat. Ut wisi enim ad minim veniamdolor sit amet, consectetuer adipiscing elit, sed diam nonummy nibh euismod tincidunt ut laoreet dolore magna aliquam erat volutpat. Ut wisi enim ad minim. ut laoreet dolore magna aliquam erat volutpat. Ut wisi enim ad minim veniamdolor sit amet, consectetuer. Lorem ipsum dolor sit amet, consectetuer adipiscing elit, sed diam nonummy nibh euismod tin ut laoreet dolore magna aliquam erat volutpat. Ut wisi enim ad minim veniam. dolor sit amet, consecuer adipiscing elit, sed diam nonummy nibh euismod tincidunt ut laoreet dolore magna aliquam erat vtpat.</p>
  <div class="btn-more abs">Read More</div>

  <form class="appointment abs">
    <h2>Schedule <span>An Appointment</span></h2>
    <label class="field-label abs" style="top:84px">Your Name</label>
    <div class="field abs" style="top:96px"></div>
    <label class="field-label abs" style="top:148px">Your Email</label>
    <div class="field abs" style="top:162px"></div>
    <label class="field-label abs" style="top:214px">Mobile No.</label>
    <div class="field abs" style="top:227px"></div>
    <label class="field-label abs" style="top:282px">Query.</label>
    <div class="field abs" style="top:295px;height:68px"></div>
    <div class="btn-more abs">SUBMIT</div>
  </form>
</section>

<section class="services abs">
  <h2 class="section-title center-title abs" style="top:47px;color:var(--white)">Our <span>Services</span></h2>
  <div class="divider abs" style="top:97px"></div>
  <div class="drop abs" style="left:594px;top:90px"></div>

  <div class="service abs" style="left:105px;top:136px">
    <svg class="service-icon" viewBox="0 0 170 77"><ellipse cx="85" cy="38.5" rx="82" ry="35" fill="none" stroke="#1f3f9e" stroke-width="4"/><rect x="68" y="24" width="34" height="14" fill="none" stroke="#111" stroke-width="3"/><path d="M72 38v14M80 38v14M90 38v14M98 38v14" stroke="#111" stroke-width="3"/></svg>
    <h3>SERVICE ONE</h3>
    <p>dolor sit amet, consectetuer adipiscing, sed diam nonummy nibh euismod tin ut laoreet dolore magna aliquam erat volutpat.</p>
    <div class="btn-more">Read More</div>
  </div>
  <div class="service abs" style="left:450px;top:136px">
    <svg class="service-icon" viewBox="0 0 170 77"><ellipse cx="85" cy="38.5" rx="82" ry="35" fill="none" stroke="#1f3f9e" stroke-width="4"/><rect x="70" y="22" width="24" height="32" rx="10" fill="none" stroke="#111" stroke-width="3"/><path d="M94 38h10v10M64 56h44" stroke="#111" stroke-width="3" fill="none"/></svg>
    <h3>SERVICE TWO</h3>
    <p>dolor sit amet, consectetuer adipiscing, sed diam nonummy nibh euismod tin ut laoreet dolore magna aliquam erat volutpat.</p>
    <div class="btn-more">Read More</div>
  </div>
  <div class="service abs" style="left:793px;top:136px">
    <svg class="service-icon" viewBox="0 0 170 77"><ellipse cx="85" cy="38.5" rx="82" ry="35" fill="none" stroke="#1f3f9e" stroke-width="4"/><path d="M64 38l21-16 21 16" fill="none" stroke="#111" stroke-width="3"/><rect x="69" y="37" width="32" height="16" fill="#111"/><path d="M58 56h54" stroke="#111" stroke-width="3"/></svg>
    <h3>SERVICE THREE</h3>
    <p>dolor sit amet, consectetuer adipiscing, sed diam nonummy nibh euismod tin ut laoreet dolore magna aliquam erat volutpat.</p>
    <div class="btn-more">Read More</div>
  </div>
</section>

<section class="testimonials">
  <h2 class="section-title center-title abs">Customer <span>Says</span></h2>
  <div class="divider abs" style="top:1638px;background:#d8d8d8"></div>
  <div class="drop abs" style="left:594px;top:1631px"></div>

  <article class="card abs" style="left:110px">
    <blockquote><span class="q">“</span> Contrary to popular belief, Lorem Ipsum is not simply random text. It has roots in a piece of classical Latin literature from 45 BC, making it over 2000 years old. Anselm <span class="q">”</span></blockquote>
    <hr><cite>CUSTOMER NAME</cite>
  </article>
  <article class="card abs" style="left:450px">
    <blockquote><span class="q">“</span> Contrary to popular belief, Lorem Ipsum is not simply random text. It has roots in a piece of classical Latin literature from 45 BC, making it over 2000 years old. Anselm <span class="q">”</span></blockquote>
    <hr><cite>CUSTOMER NAME</cite>
  </article>
  <article class="card abs" style="left:788px">
    <blockquote><span class="q">“</span> Contrary to popular belief, Lorem Ipsum is not simply random text. It has roots in a piece of classical Latin literature from 45 BC, making it over 2000 years old. Anselm <span class="q">”</span></blockquote>
    <hr><cite>CUSTOMER NAME</cite>
  </article>

  <svg class="avatar abs" style="left:214px" viewBox="0 0 94 107"><polygon points="47,0 94,27 94,80 47,107 0,80 0,27" fill="#ececec"/></svg>
  <svg class="avatar abs" style="left:554px" viewBox="0 0 94 107"><polygon points="47,0 94,27 94,80 47,107 0,80 0,27" fill="#ececec"/></svg>
  <svg class="avatar abs" style="left:892px" viewBox="0 0 94 107"><polygon points="47,0 94,27 94,80 47,107 0,80 0,27" fill="#ececec"/></svg>
</section>

<svg class="wave abs" viewBox="0 0 1200 190" preserveAspectRatio="none">
  <path d="M0 120 C200 90 420 100 560 150 L640 150 C800 110 1000 70 1200 40 L1200 190 L0 190Z" fill="#1f1f1f"/>
  <path d="M0 112 C220 80 420 92 560 140" fill="none" stroke="#1f3f9e" stroke-width="14"/>
  <path d="M640 146 C820 104 1020 66 1200 30" fill="none" stroke="#3d8fca" stroke-width="14"/>
  <ellipse cx="600" cy="150" rx="105" ry="42" fill="#fff"/>
</svg>
<div class="wave-brand abs">Velmora</div>

<footer>
  <div class="site-footer abs"></div>

  <h3 class="footer-heading abs" style="left:110px;top:2168px">Quick Links</h3>
  <div class="footer-rule abs" style="left:110px;top:2198px;width:168px"></div>
  <ul class="quick-links abs">
    <li>Home</li><li>About</li><li>Products</li><li>Free Estimates</li><li>Schedule An Appointment</li><li>Contact</li>
  </ul>

  <h3 class="footer-heading abs" style="left:346px;top:2168px">Contact Detail</h3>
  <div class="footer-rule abs" style="left:346px;top:2198px;width:470px"></div>
  <div class="contact-item abs" style="top:2208px;width:240px">
    <svg width="12" height="16" viewBox="0 0 12 16"><path d="M6 0a6 6 0 0 1 6 6c0 4-6 10-6 10S0 10 0 6a6 6 0 0 1 6-6z" fill="#fff"/><circle cx="6" cy="6" r="2.2" fill="#1f1f1f"/></svg>
    <span>Lorem ipsum dolor sit consectetuer adipiscing elit, diam nonummy nibh</span>
  </div>
  <div class="contact-item abs" style="top:2246px">
    <svg width="12" height="14" viewBox="0 0 12 14"><path d="M2 0l3 3-2 2c1 2 2 4 4 5l2-2 3 3-2 3C4 13 0 7 0 2z" fill="#fff"/></svg>
    <span>100 555 0142</span>
  </div>
  <div class="contact-item abs" style="top:2283px">
    <svg width="13" height="13" viewBox="0 0 13 13"><rect x="3" y="0" width="7" height="4" fill="#fff"/><rect x="0" y="4" width="13" height="6" fill="#fff"/><rect x="3" y="8" width="7" height="5" fill="#fff" stroke="#1f1f1f"/></svg>
    <span>100 555 0187</span>
  </div>
  <div class="contact-item abs" style="top:2317px">
    <svg width="13" height="10" viewBox="0 0 13 10"><rect width="13" height="10" fill="#fff"/><path d="M0 0l6.5 5L13 0" fill="none" stroke="#1f1f1f"/></svg>
    <span>hello@velmora-water.example</span>
  </div>
  <div class="map abs" role="img" aria-label="Street map showing the office location"></div>

  <h3 class="footer-heading abs" style="left:875px;top:2168px">Newsletter Sign Up</h3>
  <div class="footer-rule abs" style="left:875px;top:2198px;width:215px"></div>
  <p class="newsletter-text abs">Stay connected and receive email updates from Us</p>
  <div class="newsletter-input abs">Enter your email here</div>
  <div class="btn-subscribe abs">SUBSCRIBE</div>

  <div class="footer-bar abs"></div>
  <span class="social abs" style="left:113px"></span>
  <span class="social abs" style="left:147px"></span>
  <span class="social abs" style="left:181px"></span>
  <span class="social abs" style="left:216px"></span>
  <span class="social abs" style="left:250px"></span>
  <p class="copyright abs">Copyright © 2017 Velmora. All Rights Reserved</p>
</footer>

</body>
</html>
```